Help make our corporate website modern and cool with graphical elements and icons

We are makers of cloud infrastructure software (www.nimbrotek.com) and our target audience is developers. Developers generally want text and icons, they don't care for photos. They want good usability and easy-to-find information. Think forkhive.com, cloud.zephyrqa.com, www.stackmoor.com, pallork.com for reference.

Your challenge will be to modernize the site and make it look "cool" from a developer's point-of-view while still keeping the basic site structure. You can add graphical elements that make the pages come more alive, suggest different layout options, and incorporate icons that we've recently developed (I've attached them for your review). We will keep the Nimbrotek blue and gray, but you are free to add complementary colors in your designs to help spice up the page. See the complementary colors we've used in the icons package.

A successful design will keep the core identity of our website but will make the pages more exciting and compelling to visit, and make the visitor want to scroll and click to dive in deeper into the site. I also want to see additional mock-ups for the main landing pages (Why Nimbrotek, Products, Community, and a new landing page for Resources).

We use WordPress and the Q theme, so if you have familiarity with that theme and its capabilities, even better.

Target Market(s)

Mobile and Web application developers from larger organizations. Developers typically don't like stock images of people or landscapes, they usually just want the information they're looking for presented in a clean and organized way. That said, they do like it if an icon or design element helps them visualize the information. So the design should be useful and necessary to the info provided.

Industry/Entity Type

Computer Software

Number of Pages Required

5+ page

Font styles to use
Sans Serif
Other font styles liked:
• We use Lato as our main font

Colors

Designer to choose colors to be used in the design.

Requirements
Must have
• Must haves:
• - clean and modern design, not too busy but still visually engaging
• - keep the core identity of the site while adding graphical elements/icons
• - use either the hexagons from the icons or incorporate the venn diagram shape somehow from https://www.nimbrotek.com/why-nimbrotek/
• - shapes and icons are preferred over photos or stock "tech" images
• - should keep the nimbrotek blue and gray but can have complementary accent colors (see the icon colors that I've attached)
• - you can use the attached icons
• - make the information appealing to view, scroll and click through
• - design must not interfere with navigation or readability, must complement and be appropriate for the specific information shown
• - use pallork.com and cloud.zephyrqa.com for reference
Nice to have
• nice to haves:
• - familiarity with Zephyrqa Run Engine and cloud computing
• - easy to implement on WordPress, familiarity with Q theme a plus
• - ability to identify with app developers
Should not have
• - unfortunately, stock photos of people or landscapes won't work
• - don't use clip art of clouds or other stock images of high tech
• - don't make it too busy, we are looking for clean and modern

```html
<!DOCTYPE html>
<html lang="en">
<head>
<meta charset="utf-8">
<title>Nimbrotek — Multi cloud native</title>
<link href="https://fonts.googleapis.com/css2?family=Jost:wght@400;500;600&family=Lato:wght@400;700;900&display=swap" rel="stylesheet">
<style>
:root{
  --blue:#1a9ad6;
  --blue-light:#3cb6ea;
  --blue-dark:#0b4ea2;
  --navy:#0a3583;
  --sky:#d4ecf9;
  --gray:#5b6470;
  --gray-light:#f1f3f5;
  --line:#e1e5ea;
  --ink:#1f2a36;
  --white:#ffffff;
}
*{box-sizing:border-box;margin:0;padding:0}
html,body{width:1200px;height:5389px;overflow:hidden}
body{font-family:"Lato",sans-serif;color:var(--gray);background:var(--white);position:relative}
.abs{position:absolute}
h1,h2,h3{font-family:"Jost",sans-serif;font-weight:500}
.section-title{color:var(--blue-dark);font-size:40px;line-height:1.2;text-align:center;font-weight:500}
.read-more{color:var(--blue);font-size:14px;font-weight:700;letter-spacing:.5px;text-transform:uppercase}
.read-more::after{content:" ⟶";font-weight:400}
.placeholder{border-radius:4px}

/* Header / hero */
.hero{left:0;top:0;width:1200px;height:560px;background:linear-gradient(120deg,#1c8fd2 0%,#2aaee6 60%,#5cc6ef 100%);clip-path:polygon(0 0,100% 0,100% 78%,0 100%)}
.hero-fade{left:0;top:380px;width:1200px;height:210px;background:linear-gradient(90deg,#bfe4f7,#e6f5fc);clip-path:polygon(0 85%,100% 0,100% 40%,0 100%)}
.logo{left:78px;top:28px;color:var(--white);font-family:"Lato",sans-serif;font-size:40px;font-weight:700}
.nav{left:360px;top:46px;display:flex;gap:34px;color:var(--white);font-size:16px}
.nav .search{width:18px;height:18px}
.hero-title{left:78px;top:150px;width:560px;color:var(--white);font-size:50px;line-height:1.12;font-weight:400}
.hero-copy{left:78px;top:310px;width:390px;color:var(--white);font-size:15px;line-height:1.5}
.btn{display:inline-block;height:50px;line-height:50px;padding:0 36px;font-size:15px;font-weight:700;letter-spacing:.5px;text-transform:uppercase}
.btn-solid{background:var(--white);color:var(--blue)}
.btn-ghost{border:2px solid var(--white);color:var(--white);line-height:46px}
.hero-actions{left:78px;top:392px;display:flex;gap:22px}
.hero-art{left:660px;top:70px;width:470px;height:350px;background:radial-gradient(circle at 50% 55%,rgba(255,255,255,.55),rgba(255,255,255,.1) 70%)}

/* Calculator */
.calc-art{left:60px;top:640px;width:300px;height:360px;background:linear-gradient(160deg,#e8f4fb,#cfe6f5)}
.calc-title{left:512px;top:658px;color:var(--ink);font-size:34px}
.calc-copy{left:512px;top:730px;width:600px;font-size:15px;line-height:1.7}
.calc-link{left:512px;top:900px}
.pager{display:flex;gap:10px}
.pager span{width:34px;height:34px;border-radius:50%;background:var(--blue-dark);color:#fff;display:flex;align-items:center;justify-content:center;font-size:15px}
.pager span:first-child{background:var(--blue)}
.calc-pager{left:512px;top:955px}

/* Partner band */
.partner-band{left:70px;top:1100px;width:1080px;height:180px;background:linear-gradient(90deg,var(--navy),var(--blue-dark) 70%,#1a5fc0);clip-path:polygon(0 22%,100% 0,100% 78%,0 100%)}
.partner-row{left:140px;top:1160px;width:960px;display:flex;justify-content:space-between;align-items:center;color:var(--white);font-size:20px;font-weight:700}

/* Portability */
.port-title{left:200px;top:1335px;width:800px}
.features{left:80px;top:1465px;width:1040px;display:flex;justify-content:space-between}
.feature{width:240px;text-align:center}
.feature h3{font-family:"Lato",sans-serif;font-weight:700;color:var(--ink);font-size:19px;margin:22px 0 10px}
.feature p{font-size:13px;line-height:1.6}
.hex-icon{width:110px;height:110px;display:block;margin:0 auto}

/* Steps */
.steps-bg{left:0;top:1770px;width:1200px;height:690px;background:linear-gradient(180deg,#e4f3fb 0%,#8fd0f0 45%,#cfe9f8 100%)}
.steps-title{left:200px;top:1845px;width:800px;font-size:38px}
.step{width:230px;color:var(--white);font-size:13px;line-height:1.5}
.step h3{font-family:"Lato",sans-serif;font-size:20px;font-weight:700;margin-bottom:6px}
.step-2{left:480px;top:1925px;text-align:center;width:240px}
.step-1{left:140px;top:2100px;text-align:center}
.step-3{left:840px;top:2100px}
.steps-hex{left:430px;top:1990px;width:340px;height:360px}

/* Benefits */
.benefits-title{left:150px;top:2455px;width:900px}
.cases{left:80px;top:2625px;width:1040px;display:flex;gap:14px}
.case{width:250px;height:290px;background:var(--white);border:1px solid var(--line);box-shadow:0 6px 18px rgba(10,53,131,.12);padding:30px 24px}
.case h3{font-family:"Lato",sans-serif;font-size:22px;font-weight:700;color:var(--ink);margin-bottom:12px}
.case p{font-size:13px;line-height:1.6;margin-bottom:22px}

/* Testimonial */
.quote-band{left:80px;top:2985px;width:1040px;height:250px;background:linear-gradient(90deg,var(--navy),var(--blue-dark) 60%,var(--blue));clip-path:polygon(0 0,100% 10%,100% 100%,0 90%)}
.quote-text{left:230px;top:3060px;width:560px;color:var(--white);font-size:18px;line-height:1.55;text-align:center}
.quote-name{left:540px;top:3140px;width:250px;color:var(--white);text-align:right}
.quote-name strong{display:block;font-size:18px;letter-spacing:1px}
.quote-name span{font-size:12px}
.quote-avatar{left:820px;top:3045px;width:120px;height:120px;border-radius:50%;background:linear-gradient(140deg,#c9d4de,#7d8b98);border:4px solid var(--white)}
.quote-pager{left:222px;top:3150px}
.quote-pager span{background:var(--white);color:var(--blue-dark)}

/* Clients */
.clients-title{left:150px;top:3275px;width:900px;font-size:38px}
.client-row{left:120px;top:3430px;width:960px;display:flex;justify-content:space-between;align-items:center;font-size:26px;font-weight:700;color:var(--blue-dark)}

/* Why */
.why-bg{left:0;top:3595px;width:1200px;height:290px;background:linear-gradient(100deg,#b8c4cf,#dfe6ec 55%,#9aa7b4)}
.why-panel{left:0;top:3595px;width:600px;height:290px;background:linear-gradient(90deg,var(--blue),var(--blue-light));clip-path:polygon(0 0,100% 0,82% 100%,0 100%)}
.why-title{left:78px;top:3630px;color:var(--white);font-size:38px}
.why-copy{left:78px;top:3700px;width:400px;color:var(--white);font-size:14px;line-height:1.6}
.why-link{left:78px;top:3840px;color:var(--white)}
.play{left:855px;top:3690px;width:90px;height:90px}

/* Blog */
.blog-title{left:200px;top:3920px;width:800px;font-size:38px}
.posts{left:80px;top:4000px;width:1040px;display:flex;justify-content:space-between}
.post{width:325px;position:relative}
.post-media{height:290px;background:linear-gradient(150deg,#3d4f63,#8fa4b8)}
.post-date{position:absolute;left:0;top:232px;width:64px;height:80px;background:var(--blue);color:#fff;text-align:center;font-family:"Jost",sans-serif;padding-top:8px}
.post-date b{display:block;font-size:26px;font-weight:500;line-height:1}
.post-date small{font-size:13px;letter-spacing:1px}
.post h3{font-family:"Lato",sans-serif;font-size:19px;font-weight:700;color:var(--blue);line-height:1.3;margin:10px 0 14px 78px;min-height:50px}
.post p{font-size:14px;line-height:1.6;margin-bottom:18px}

/* Contact */
.contact-bg{left:0;top:4560px;width:1200px;height:560px;background:var(--gray-light)}
.contact-card{left:215px;top:4580px;width:770px;height:470px;background:var(--white);box-shadow:0 8px 24px rgba(0,0,0,.08)}
.contact-title{left:215px;top:4625px;width:770px;text-align:center;color:var(--blue-dark);font-size:34px}
.field{position:absolute;height:58px;border:1px solid var(--line);background:#fafbfc;font-size:13px;color:#8a93a0;padding:20px 16px}
.submit{left:535px;top:4975px;height:56px;width:130px;background:var(--blue);color:#fff;font-weight:700;font-size:15px;text-align:center;line-height:56px;text-transform:uppercase}

/* Footer */
.footer{left:0;top:5010px;width:1200px;height:320px;background:linear-gradient(90deg,var(--blue) 0%,#1587cb 50%,var(--blue-dark) 100%);clip-path:polygon(0 22%,100% 0,100% 100%,0 100%)}
.foot-brand{left:80px;top:5140px;color:#fff;display:flex;gap:16px}
.foot-brand .pin{width:44px;height:44px}
.foot-brand strong{display:block;font-size:17px}
.foot-brand span{font-size:12px;line-height:1.5}
.foot-links{left:380px;top:5160px;color:#fff;font-size:12px;display:flex;gap:8px}
.socials{left:500px;top:5195px;display:flex;gap:8px}
.socials span{width:22px;height:22px;border-radius:50%;background:var(--white);opacity:.9}
.socials span:nth-child(2){background:#2d5fb3}
.socials span:nth-child(3){background:#e04a5a}
.foot-contact{left:880px;top:5140px;color:#fff;font-size:13px}
.foot-contact div{display:flex;align-items:center;gap:12px;margin-bottom:18px}
.foot-contact svg{width:34px;height:34px}
.copyright{left:0;top:5330px;width:1200px;height:59px;background:#0a3170;color:#fff;text-align:center;line-height:59px;font-size:14px}
</style>
</head>
<body>

<!-- Hero -->
<div class="abs hero-fade"></div>
<div class="abs hero"></div>
<div class="abs logo">Nimbrotek</div>
<nav class="abs nav">
  <span>Why Nimbrotek</span><span>Products</span><span>Community</span><span>Resources</span><span>Try Nimbrotek</span><span>Contact Us</span>
  <svg class="search" viewBox="0 0 20 20"><circle cx="8" cy="8" r="6" fill="none" stroke="#fff" stroke-width="2"/><path d="M13 13l5 5" stroke="#fff" stroke-width="2"/></svg>
</nav>
<h1 class="abs hero-title">Multi cloud native. Serverless by design. NoOps as a first principle.</h1>
<p class="abs hero-copy">Nimbrotek is an easy-to-manage serverless platform for building and running scalable web and mobile applications on any infrastructure. Build your app rapidly for multi cloud deployment.</p>
<div class="abs hero-actions"><span class="btn btn-solid">Why Nimbrotek</span><span class="btn btn-ghost">Try it free</span></div>
<div class="abs hero-art placeholder" role="img" aria-label="Line illustration of a developer dashboard with charts, monitor and connected cloud icons"></div>

<!-- Calculator -->
<div class="abs calc-art placeholder" role="img" aria-label="Line illustration of a laptop linked to many cloud services"></div>
<h2 class="abs calc-title">Calculate the Cost to Migrate loud</h2>
<p class="abs calc-copy">Use our free tool to calculate how much your Zephyrqa Run Engine (ZRE) application would cost if you migrated it to one of five different public clouds (including Zephyrqa Compute Engine). Lorem Ipsum is simply dummy text of the printing and typesetting industry. Lorem Ipsum has been the industry's standard dummy text ever since the 1500s, when an unknown printer took a galley of type and scrambled it to make a type specimen book. It has survived not only five centuries.</p>
<span class="abs read-more calc-link">Try the calculator</span>
<div class="abs pager calc-pager"><span>‹</span><span>›</span></div>

<!-- Partners -->
<div class="abs partner-band"></div>
<div class="abs partner-row">
  <span>Vantor Web</span><span>Zephyrqa</span><span>Kestrel Cloud</span><span>Orvane Cloud</span><span>Tessaro</span><span>Celvix</span><span>Pillarnet</span>
</div>

<!-- Portability -->
<h2 class="abs section-title port-title">Nimbrotek enables serverless development with application portability</h2>
<div class="abs features">
  <div class="feature">
    <svg class="hex-icon" viewBox="0 0 110 110"><polygon points="55,4 100,30 100,80 55,106 10,80 10,30" fill="#1a9ad6"/><rect x="35" y="42" width="40" height="26" rx="3" fill="none" stroke="#fff" stroke-width="3"/><path d="M28 60h-6M88 60h-6" stroke="#fff" stroke-width="3"/></svg>
    <h3>Multi Cloud Migration</h3><p>Migrate between major public cloud providers with no code changes, for cost-savings and business alignment.</p>
  </div>
  <div class="feature">
    <svg class="hex-icon" viewBox="0 0 110 110"><polygon points="55,4 100,30 100,80 55,106 10,80 10,30" fill="#1a9ad6"/><circle cx="55" cy="55" r="18" fill="none" stroke="#fff" stroke-width="3"/><path d="M37 55h36M55 37v36" stroke="#fff" stroke-width="3"/></svg>
    <h3>Hybrid Cloud</h3><p>Run cloud-native apps in public cloud and on premises, even in isolated or resource-constrained environments.</p>
  </div>
  <div class="feature">
    <svg class="hex-icon" viewBox="0 0 110 110"><polygon points="55,4 100,30 100,80 55,106 10,80 10,30" fill="#1a9ad6"/><rect x="38" y="38" width="34" height="34" fill="none" stroke="#fff" stroke-width="3"/><path d="M46 50h18M46 60h18" stroke="#fff" stroke-width="3"/></svg>
    <h3>Serverless Platform</h3><p>Increase developer productivity using high-level APIs on a platform with load balancing and auto-scaling.</p>
  </div>
  <div class="feature">
    <svg class="hex-icon" viewBox="0 0 110 110"><polygon points="55,4 100,30 100,80 55,106 10,80 10,30" fill="#1a9ad6"/><circle cx="55" cy="55" r="16" fill="none" stroke="#fff" stroke-width="3"/><path d="M55 31v8M55 71v8M31 55h8M71 55h8" stroke="#fff" stroke-width="3"/></svg>
    <h3>NoOps</h3><p>Escape cloud lock-in, minimize costs, and future-proof your application, all without assuming operational burden.</p>
  </div>
</div>

<!-- Steps -->
<div class="abs steps-bg"></div>
<h2 class="abs section-title steps-title">Get started in 3 easy steps</h2>
<div class="abs step step-2"><h3>2 Write your app</h3>Write your application in Python, Java, Go, or PHP. Point Nimbrotek at your code and let it take care of the rest.</div>
<div class="abs step step-1"><h3>1 Install Nimbrotek</h3>Run Nimbrotek on any supported platform or use ours as a sandbox. Easily set up on Vantor, Zephyrqa, Celvix, or Pillarnet.</div>
<div class="abs step step-3"><h3>3 Run your app</h3>Nimbrotek will immediately scale your application and manage load balancing for hosting and service traffic.</div>
<svg class="abs steps-hex" viewBox="0 0 340 360">
  <polygon points="170,20 310,100 310,260 170,340 30,260 30,100" fill="#ffffff"/>
  <polygon points="170,0 204,20 204,60 170,80 136,60 136,20" fill="#0b4ea2"/>
  <path d="M160 30l-10 10 10 10M180 30l10 10-10 10" stroke="#fff" stroke-width="3" fill="none"/>
  <polygon points="20,160 54,180 54,220 20,240 -14,220 -14,180" transform="translate(14 0)" fill="#0b4ea2"/>
  <rect x="22" y="186" width="24" height="18" fill="none" stroke="#fff" stroke-width="3"/>
  <polygon points="306,160 340,180 340,220 306,240 272,220 272,180" transform="translate(-14 0)" fill="#0b4ea2"/>
  <path d="M282 214v-8M292 214v-16M302 214v-24" stroke="#fff" stroke-width="4"/>
  <rect x="130" y="110" width="80" height="26" rx="13" fill="#1a9ad6"/>
  <text x="170" y="128" fill="#fff" font-family="Lato,sans-serif" font-size="11" font-weight="700" text-anchor="middle">TRY NIMBROTEK</text>
  <rect x="90" y="150" width="160" height="130" fill="#e3eef6" role="img" aria-label="Illustration of a developer working at a laptop"/>
</svg>

<!-- Benefits -->
<h2 class="abs section-title benefits-title">Nimbrotek benefits developers, operations, and the organization with a serverless platform for multi cloud deployment.</h2>
<div class="abs cases">
  <div class="case"><h3>Larkmoor Apparel</h3><p>Cloud migration from Zephyrqa Run Engine to mainland China with no modifications or proxy servers.</p><span class="read-more">Read more</span></div>
  <div class="case"><h3>Tilvane</h3><p>Cloud native application enabled for on-premises deployments for better security and control.</p><span class="read-more">Read more</span></div>
  <div class="case"><h3>Quarrow</h3><p>Hybrid cloud implementation for paid and freemium customers to reduce overall cloud costs.</p><span class="read-more">Read more</span></div>
  <div class="case"><h3>Brightfold Retail</h3><p>Cloud migration to Celvix Cloud for improved performance and reliability and developer flexibility.</p><span class="read-more">Read more</span></div>
</div>

<!-- Testimonial -->
<div class="abs quote-band"></div>
<p class="abs quote-text">With Nimbrotek you can run your Run Engine app on any physical or cloud infrastructure, wherever you want.</p>
<div class="abs quote-name"><strong>DORIAN CALLOWAY</strong><span>Director, Solutions Zephyrqa Cloud Platform</span></div>
<div class="abs quote-avatar" role="img" aria-label="Portrait photo of the quoted director"></div>
<div class="abs pager quote-pager"><span>‹</span><span>›</span></div>

<!-- Clients -->
<h2 class="abs section-title clients-title">Successful startups and innovative companies choose Nimbrotek</h2>
<div class="abs client-row"><span>Loomvale</span><span>Brenhold</span><span>Quorra</span><span>Feltmark</span><span>Wildtrust</span></div>

<!-- Why -->
<div class="abs why-bg placeholder" role="img" aria-label="Photo of two colleagues reviewing work at a desk"></div>
<div class="abs why-panel"></div>
<h2 class="abs why-title">Why Nimbrotek...?</h2>
<p class="abs why-copy">Lorem Ipsum is simply dummy text of the printing and typesetting industry. Lorem Ipsum has been the industry's standard dummy text ever since the 1500s, when an unknown printer took a galley of type and scrambled it to make a type specimen book. It has survived not only five centuries.</p>
<span class="abs read-more why-link">Read more</span>
<svg class="abs play" viewBox="0 0 90 90"><circle cx="45" cy="45" r="44" fill="#ffffff"/><polygon points="36,28 64,45 36,62" fill="#1f2a36"/></svg>

<!-- Blog -->
<h2 class="abs section-title blog-title">Recent Blog &amp; News</h2>
<div class="abs posts">
  <article class="post"><div class="post-media placeholder" role="img" aria-label="Photo of a server room aisle"></div><div class="post-date"><b>02</b><small>FEB</small></div><h3>Lorem Ipsum printing of typesetting industry.</h3><p>Lorem Ipsum is simply dummy text of the printing and typesetting industry. Lorem Ipsum has been the industry's standard dummy.</p><span class="read-more">Read more</span></article>
  <article class="post"><div class="post-media placeholder" role="img" aria-label="Photo of a hand touching a network of floating icons"></div><div class="post-date"><b>02</b><small>FEB</small></div><h3>Lorem Ipsum printing of typesetting industry.</h3><p>Lorem Ipsum is simply dummy text of the printing and typesetting industry. Lorem Ipsum has been the industry's standard dummy.</p><span class="read-more">Read more</span></article>
  <article class="post"><div class="post-media placeholder" role="img" aria-label="Photo of a person working on a laptop"></div><div class="post-date"><b>02</b><small>FEB</small></div><h3>Lorem Ipsum printing of typesetting industry.</h3><p>Lorem Ipsum is simply dummy text of the printing and typesetting industry. Lorem Ipsum has been the industry's standard dummy.</p><span class="read-more">Read more</span></article>
</div>

<!-- Contact -->
<div class="abs contact-bg"></div>
<div class="abs contact-card"></div>
<h2 class="abs contact-title">Contact Us</h2>
<div class="field" style="left:285px;top:4710px;width:308px">First Name :</div>
<div class="field" style="left:607px;top:4710px;width:308px">Last Name :</div>
<div class="field" style="left:285px;top:4785px;width:308px">Email :</div>
<div class="field" style="left:607px;top:4785px;width:308px">Company Name :</div>
<div class="field" style="left:285px;top:4860px;width:630px;height:95px">Message :</div>
<div class="abs submit">Submit</div>

<!-- Footer -->
<footer class="abs footer"></footer>
<div class="abs foot-brand">
  <svg class="pin" viewBox="0 0 44 44"><circle cx="22" cy="22" r="21" fill="#fff"/><path d="M22 11a7 7 0 0 0-7 7c0 6 7 14 7 14s7-8 7-14a7 7 0 0 0-7-7z" fill="#0b4ea2"/><circle cx="22" cy="18" r="2.5" fill="#fff"/></svg>
  <div><strong>Nimbrotek Systems, Inc.</strong><span>1423 Larkspur Road, Suite 200<br>Eastbrook, CA 90000</span></div>
</div>
<div class="abs foot-links"><span>Get Started</span>|<span>Team</span>|<span>Careers</span>|<span>Press</span>|<span>Partners</span>|<span>Contact Us</span></div>
<div class="abs socials"><span></span><span></span><span></span><span></span></div>
<div class="abs foot-contact">
  <div><svg viewBox="0 0 34 34"><circle cx="17" cy="17" r="16" fill="#fff"/><path d="M12 9l3 0 2 5-2 1.5a9 9 0 0 0 4 4l1.5-2 5 2v3a2 2 0 0 1-2 2A14 14 0 0 1 10 11a2 2 0 0 1 2-2z" fill="#0b4ea2"/></svg>(555) 014-2273</div>
  <div><svg viewBox="0 0 34 34"><circle cx="17" cy="17" r="16" fill="#fff"/><rect x="9" y="11" width="16" height="12" fill="none" stroke="#0b4ea2" stroke-width="2"/><path d="M9 11l8 7 8-7" fill="none" stroke="#0b4ea2" stroke-width="2"/></svg>support@nimbrotek.com</div>
</div>
<div class="abs copyright">© 2018 <b>NIMBROTEK</b>. All rights reserved.</div>

</body>
</html>
```